4th Generation Family Business Needs a New Card Design!

We are a family owned 4th Generation company. We are based in the Sydney, Australia area and we are desperately in need of a more modern and classy card. We are monumental masons who design, supply & erect lasting memorials throughout cemeteries in Sydney. Our customers are normally in a period of grieving. I have attached logo files that will need to be implemented on the card. Company was established 1935. Australian Owned and Operated. Card needs to be designed to PRINTLY.com specification.

Target Market(s)

Our target market is based upon people that a grieving for family members that have passed away. We also deal with alot of companies that own and operate cemeteries.

Industry/Entity Type

Business

Contact Information for Business Card

Oliver Brantley, Operations Manager, 0417552908, oliver@hollowaystoneworks.com.au
Martin Brantley, Director, 0431906627, martin@hollowaystoneworks.com.au
Phone # 02 9634 2258
Website: www.hollowaystoneworks.com.au
Address: Suite 17, 8 Calloway Lane, East Penrose, Sydney NSW 2290

Font styles to use
Serif
Decorative
Script

Requirements
Must have
• Would like to see the logo nicely implemented with a modern design. Embossed lettering would be a nice additive.

```html
<!DOCTYPE html>
<html lang="en">
<head>
<meta charset="utf-8">
<title>Holloway Stoneworks – Business Card</title>
<link rel="stylesheet" href="https://fonts.googleapis.com/css2?family=Cinzel:wght@600&family=Libre+Baskerville:ital,wght@0,400;1,400;1,700&display=swap">
<style>
  :root {
    --backdrop: #3b302b;
    --card: #141414;
    --card-edge: #0b0b0b;
    --ink: #f4f2ee;
    --gold: #e3ad1f;
    --muted: #cfcac2;
  }
  * { box-sizing: border-box; margin: 0; padding: 0; }
  html, body { width: 1200px; height: 900px; overflow: hidden; }
  body {
    background: var(--backdrop);
    font-family: "Libre Baskerville", Georgia, serif;
    color: var(--ink);
    position: relative;
  }
  .card {
    position: absolute;
    top: 291px;
    width: 520px;
    height: 318px;
    background: var(--card);
    border: 1px solid var(--card-edge);
    box-shadow: 0 14px 30px rgba(0,0,0,0.45);
  }
  .card--back { left: 50px; }
  .card--front { left: 630px; }

  .wordmark {
    font-family: "Cinzel", "Times New Roman", serif;
    font-weight: 600;
    color: var(--ink);
    text-align: center;
    line-height: 1.05;
    letter-spacing: 0.04em;
  }
  .card--back .wordmark {
    position: absolute;
    left: 26px;
    top: 88px;
    width: 210px;
    font-size: 27px;
  }
  .card--front .wordmark {
    position: absolute;
    left: 0;
    right: 0;
    top: 104px;
    font-size: 38px;
  }

  .contacts {
    position: absolute;
    left: 262px;
    top: 30px;
    width: 250px;
  }
  .person + .person { margin-top: 12px; }
  .person__name {
    font-style: italic;
    font-weight: 700;
    font-size: 17px;
    line-height: 1.2;
  }
  .person__role {
    color: var(--gold);
    font-size: 12px;
    line-height: 1.4;
  }
  .person__line {
    display: flex;
    align-items: center;
    gap: 7px;
    font-size: 12px;
    line-height: 1.55;
    color: var(--muted);
  }
  .icon { width: 12px; height: 12px; flex: none; }

  .company-details {
    position: absolute;
    left: 0;
    right: 0;
    bottom: 22px;
    text-align: center;
    font-size: 12px;
    line-height: 1.5;
    color: var(--muted);
  }
  .front-url {
    position: absolute;
    left: 0;
    right: 0;
    top: 226px;
    text-align: center;
    font-size: 12px;
    color: var(--muted);
  }
</style>
</head>
<body>

<section class="card card--back" aria-label="Business card, contact side">
  <div class="wordmark">HOLLOWAY<br>STONEWORKS</div>

  <div class="contacts">
    <div class="person">
      <p class="person__name">Oliver Brantley</p>
      <p class="person__role">Operations Manager</p>
      <p class="person__line">
        <svg class="icon" viewBox="0 0 12 12" aria-hidden="true"><rect width="12" height="12" rx="1.5" fill="#e3ad1f"/><path d="M3.4 2.6l1.3 1.2-.6 1.1c.5 1 1.3 1.8 2.3 2.3l1.1-.6 1.2 1.3-.8.9C5.7 8.6 3.4 6.3 2.5 3.4z" fill="#141414"/></svg>
        0417552908
      </p>
      <p class="person__line">
        <svg class="icon" viewBox="0 0 12 12" aria-hidden="true"><rect width="12" height="12" rx="1.5" fill="#e3ad1f"/><rect x="2.5" y="3.5" width="7" height="5" fill="none" stroke="#141414" stroke-width="1"/><path d="M2.5 3.5L6 6.4l3.5-2.9" fill="none" stroke="#141414" stroke-width="1"/></svg>
        oliver@hollowaystoneworks.com.au
      </p>
    </div>
    <div class="person">
      <p class="person__name">Martin Brantley</p>
      <p class="person__role">Director</p>
      <p class="person__line">
        <svg class="icon" viewBox="0 0 12 12" aria-hidden="true"><rect width="12" height="12" rx="1.5" fill="#e3ad1f"/><path d="M3.4 2.6l1.3 1.2-.6 1.1c.5 1 1.3 1.8 2.3 2.3l1.1-.6 1.2 1.3-.8.9C5.7 8.6 3.4 6.3 2.5 3.4z" fill="#141414"/></svg>
        0431906627
      </p>
      <p class="person__line">
        <svg class="icon" viewBox="0 0 12 12" aria-hidden="true"><rect width="12" height="12" rx="1.5" fill="#e3ad1f"/><rect x="2.5" y="3.5" width="7" height="5" fill="none" stroke="#141414" stroke-width="1"/><path d="M2.5 3.5L6 6.4l3.5-2.9" fill="none" stroke="#141414" stroke-width="1"/></svg>
        martin@hollowaystoneworks.com.au
      </p>
    </div>
  </div>

  <div class="company-details">
    <p>Phone # 02 9634 2258</p>
    <p>www.hollowaystoneworks.com.au</p>
    <p>Suite 17, 8 Calloway Lane, East Penrose, Sydney NSW 2290</p>
  </div>
</section>

<section class="card card--front" aria-label="Business card, brand side">
  <div class="wordmark">HOLLOWAY<br>STONEWORKS</div>
  <p class="front-url">www.hollowaystoneworks.com.au</p>
</section>

</body>
</html>
```